Etiketten für Kuchen im Glas
Zielgruppe
Die Firma Brelkat bietet kulinarische Präsente und Geschenkideen zum Thema kreatives Backen an. Unsere Zielgruppe ist B2C und Werbetreibende, die unsere Produkte als Geschenke einsetzen.
Aufgabenstellung
Für unsere Zielgruppe "Feinkostläden" benötigen wir ein etwas edleres klasssisches Etiketten-Design.
Gestaltet wird der Deckel und die Vorderseite eines Etiketts für ein 290 ml FUMS-Glas. Die entsprechende Designvorlage steht hier zum Download bereit:
https://files.tralvex-speicher.de/u/4827351/7902_01358_0000-Vorlage%20CMYK%20v08_2013-09.psd
Benötigt werden 4 unterschiedliche Etiketten, die aber aus einem "Guss" sein sollten für die Sorten: Stracciatella, Schokolade, Zitrone, Stollen. Die Sorte sollte mit auf dem Etikett stehen.
Sonstige Angaben auf dem Etikett:
- optional "Kuchen im Glas"
- gerne Grünhof Logo (siehe Anhang)
- optional "fertig gebacken". Könnte z.B. gut auf dem Deckel in Kombination mit "Kuchen im Gla" stehen
Achtung: Das Etikett für die Rückseite mit Deklaration muss nicht gestaltet werden.
Tipps: Das Etikett ist konisch und das Glas rund. Das bedeutet, dass Bilder + Schriften mit einer leichten Wölbung kreiert werden sollten. Für die Wölbung kann man sich gut an der unteren Designlinie orientieren.
Farbgestaltung: eher dunkel; z.B. Grau, Dunkelblau evtl. Schwarz
Schriften: Es dürfen auch kostenpflichtige Schriften verwendet werden. Freie Schriften allerdings bevorzugt
Format: Photoshop PSD inklusive allen Ebenen und verwendeten Elementen als einzelne Ebene.
Bei Fragen gerne melden, ich freue mich auf Eure Designs.

```html
<!DOCTYPE html>
<html lang="de">
<head>
<meta charset="utf-8">
<title>Kuchen im Glas – Etikett Zitrone</title>
<link rel="stylesheet" href="https://fonts.googleapis.com/css2?family=Great+Vibes&family=Lato:wght@400;700&family=Courgette&display=swap">
<style>
  :root {
    --frame: #3a3a3a;
    --paper: #ffffff;
    --grey-dark: #8e8e8e;
    --grey-mid: #b4b4b4;
    --grey-light: #dcdcdc;
    --band: #c9c9c9;
    --gold: #f2c21b;
    --gold-dark: #d9a300;
    --ink-navy: #2b2a6b;
    --ink-grey: #6e6e6e;
    --lemon: #f5d33a;
    --name-white: #f4f4f4;
    --outline: #555555;
  }
  html, body {
    margin: 0;
    padding: 0;
    overflow: hidden;
    background: var(--paper);
  }
  .sheet {
    width: 1200px;
    height: 421px;
    box-sizing: border-box;
    border: 4px solid var(--frame);
    background: var(--paper);
  }
  .sheet svg { display: block; }
  .tagline {
    font-family: "Lato", sans-serif;
    font-size: 16px;
    letter-spacing: 1px;
    fill: var(--ink-grey);
  }
  .product-title {
    font-family: "Great Vibes", cursive;
    fill: var(--ink-navy);
  }
  .flavour {
    font-family: "Courgette", cursive;
    fill: var(--name-white);
    stroke: #6a6a6a;
    stroke-width: 1.2px;
    paint-order: stroke;
  }
  .seal-name {
    font-family: "Lato", sans-serif;
    font-weight: 400;
    font-size: 14px;
    fill: var(--name-white);
  }
</style>
</head>
<body>
<div class="sheet">
<svg width="1192" height="413" viewBox="4 4 1192 413" xmlns="http://www.w3.org/2000/svg">
  <defs>
    <radialGradient id="lid-surface" cx="50%" cy="45%" r="60%">
      <stop offset="0" stop-color="#dcdcdc"/>
      <stop offset="1" stop-color="#8e8e8e"/>
    </radialGradient>
    <linearGradient id="wrap-surface" x1="0" y1="0" x2="1" y2="0">
      <stop offset="0" stop-color="#8e8e8e"/>
      <stop offset="0.5" stop-color="#dcdcdc"/>
      <stop offset="1" stop-color="#8e8e8e"/>
    </linearGradient>
    <clipPath id="wrap-clip">
      <path d="M445,86 Q816,8 1187,86 L1187,385 Q816,291 445,385 Z"/>
    </clipPath>
    <path id="flavour-arc" d="M610,340 Q816,300 1022,340"/>
  </defs>

  <g class="lid-label">
    <circle cx="212" cy="212" r="186" fill="url(#lid-surface)" stroke="var(--outline)" stroke-width="2"
            role="img" aria-label="Grauer Rautenmuster-Hintergrund"/>
    <text class="tagline" x="212" y="78" text-anchor="middle">- FERTIG GEBACKEN -</text>
    <g class="cartouche">
      <rect x="40" y="108" width="345" height="174" rx="34" fill="var(--gold)" stroke="var(--gold-dark)" stroke-width="2"/>
      <rect x="50" y="118" width="325" height="154" rx="28" fill="var(--paper)"/>
    </g>
    <text class="product-title" x="212" y="206" text-anchor="middle" font-size="54">Kuchen im Glas</text>
    <ellipse cx="212" cy="246" rx="32" ry="16" fill="var(--lemon)"
             role="img" aria-label="Illustration: Zitronen mit Blättern"/>
    <text class="flavour" x="212" y="348" text-anchor="middle" font-size="38">Zitrone</text>
  </g>

  <g class="wrap-label">
    <g clip-path="url(#wrap-clip)">
      <rect x="445" y="0" width="745" height="421" fill="url(#wrap-surface)"
            role="img" aria-label="Grauer Rautenmuster-Hintergrund"/>
      <path d="M445,190 Q816,110 1187,190" fill="none" stroke="var(--band)" stroke-width="54" opacity="0.85"/>
    </g>
    <path d="M445,86 Q816,8 1187,86 L1187,385 Q816,291 445,385 Z" fill="none" stroke="var(--outline)" stroke-width="2"/>

    <g class="cartouche">
      <rect x="628" y="50" width="270" height="216" rx="38" fill="var(--gold)" stroke="var(--gold-dark)" stroke-width="2"/>
      <rect x="638" y="60" width="250" height="196" rx="32" fill="var(--paper)"/>
    </g>
    <text class="tagline" x="763" y="124" text-anchor="middle">- FERTIG GEBACKEN -</text>
    <text class="product-title" x="763" y="180" text-anchor="middle" font-size="44">Kuchen im Glas</text>
    <ellipse cx="763" cy="226" rx="30" ry="15" fill="var(--lemon)"
             role="img" aria-label="Illustration: Zitronen mit Blättern"/>

    <text class="flavour" font-size="32" text-anchor="middle">
      <textPath href="#flavour-arc" startOffset="50%">Zitrone</textPath>
    </text>

    <g class="seal">
      <rect x="498" y="334" width="14" height="14" fill="var(--name-white)"/>
      <text class="seal-name" x="518" y="346">Grünhof</text>
    </g>
  </g>
</svg>
</div>
</body>
</html>
```